Sheriff Candidate needs a large yard sign

A candidate for Sheriff needs to have a sign to put in front of businesses and houses that advertise her candidacy.

Target Market(s)

Democrats, voters

Industry/Entity Type

Political

Font styles to use
Sans Serif

Colors
34a7d7
3276b5

Requirements
Must have
• Must have her picture
• Must have the words "Elect Dana Whitlock" - I'd like the name Dana to be smaller Whitlock. "Elect" and "Whitlock" should be the focus.
• at the bottom in a box "Paid for by the Committee to Elect Dana Whitlock"
Nice to have
• it would be good to have her logo as well.
• blue color for democrats and on a white background
Should not have
• pink color

```html
<!DOCTYPE html>
<html lang="en">
<head>
<meta charset="utf-8">
<title>Elect Dana Whitlock – Yard Sign</title>
<link rel="stylesheet" href="https://fonts.googleapis.com/css2?family=Cinzel:wght@500&family=Open+Sans:wght@500;700&display=swap">
<style>
  :root {
    --sky: #34a7d7;
    --navy-blue: #3276b5;
    --paper: #ffffff;
    --photo-deep: #2f72b4;
    --photo-light: #5a95cf;
    --seal-gold: #c9a227;
  }
  html, body {
    margin: 0;
    padding: 0;
    overflow: hidden;
    background: var(--paper);
  }
  .yard-sign {
    position: relative;
    width: 1200px;
    height: 751px;
    background: var(--paper);
    overflow: hidden;
  }
  .star-band {
    position: absolute;
    left: 0; top: 0;
    width: 1200px; height: 92px;
    background: var(--sky);
  }
  .star-band svg { display: block; }
  .campaign-mark {
    position: absolute;
    left: 284px; top: 80px;
    width: 188px; height: 188px;
    border-radius: 50%;
    background: var(--paper);
    display: flex;
    flex-direction: column;
    align-items: center;
    justify-content: center;
    gap: 10px;
  }
  .campaign-mark .mark-dot {
    width: 22px; height: 22px;
    border-radius: 50%;
    background: var(--navy-blue);
  }
  .campaign-mark .mark-name {
    font-family: "Cinzel", serif;
    font-weight: 500;
    font-size: 19px;
    line-height: 1.15;
    text-align: center;
    color: var(--navy-blue);
    letter-spacing: 1px;
  }
  .candidate-portrait {
    position: absolute;
    left: 755px; top: 71px;
    width: 356px; height: 356px;
    border-radius: 50%;
    border: 3px solid var(--sky);
    box-sizing: border-box;
    background: var(--paper);
  }
  .candidate-portrait .portrait-fill {
    position: absolute;
    inset: 7px;
    border-radius: 50%;
    background: radial-gradient(circle at 60% 45%, var(--photo-light), var(--photo-deep));
  }
  .headline {
    position: absolute;
    left: 0; top: 0;
  }
  .headline text {
    font-family: "Cinzel", serif;
    font-weight: 500;
  }
  .headline .elect-word { fill: var(--navy-blue); }
  .headline .surname { fill: var(--navy-blue); }
  .headline .given-name { fill: var(--sky); }
  .disclaimer-band {
    position: absolute;
    left: 0; top: 681px;
    width: 1200px; height: 70px;
    background: var(--sky);
    display: flex;
    align-items: center;
    justify-content: center;
  }
  .disclaimer-band p {
    margin: 0;
    font-family: "Open Sans", sans-serif;
    font-weight: 500;
    font-size: 21px;
    letter-spacing: 1px;
    color: var(--paper);
  }
</style>
</head>
<body>
<main class="yard-sign">
  <header class="star-band">
    <svg width="1200" height="92" viewBox="0 0 1200 92" aria-hidden="true">
      <defs>
        <polygon id="band-star" fill="#ffffff"
          points="0,-14 3.3,-4.5 13.3,-4.3 5.3,1.7 8.2,11.3 0,5.6 -8.2,11.3 -5.3,1.7 -13.3,-4.3 -3.3,-4.5"/>
      </defs>
      <use href="#band-star" x="52" y="45"/>
      <use href="#band-star" x="113" y="45"/>
      <use href="#band-star" x="174" y="45"/>
      <use href="#band-star" x="235" y="45"/>
      <use href="#band-star" x="296" y="45"/>
      <use href="#band-star" x="357" y="45"/>
      <use href="#band-star" x="418" y="45"/>
      <use href="#band-star" x="479" y="45"/>
      <use href="#band-star" x="540" y="45"/>
      <use href="#band-star" x="601" y="45"/>
      <use href="#band-star" x="662" y="45"/>
      <use href="#band-star" x="723" y="45"/>
      <use href="#band-star" x="784" y="45"/>
      <use href="#band-star" x="845" y="45"/>
      <use href="#band-star" x="906" y="45"/>
      <use href="#band-star" x="967" y="45"/>
      <use href="#band-star" x="1028" y="45"/>
      <use href="#band-star" x="1089" y="45"/>
      <use href="#band-star" x="1150" y="45"/>
    </svg>
  </header>

  <div class="campaign-mark">
    <span class="mark-dot"></span>
    <span class="mark-name">Whitlock<br>for Sheriff</span>
  </div>

  <div class="candidate-portrait">
    <div class="portrait-fill" role="img" aria-label="Portrait photo of candidate Dana Whitlock smiling, on a blue background"></div>
  </div>

  <svg class="headline" width="1200" height="681" viewBox="0 0 1200 681">
    <text class="elect-word" x="84" y="420" font-size="160" textLength="508" lengthAdjust="spacingAndGlyphs">ELECT</text>
    <text class="given-name" transform="translate(146 620) rotate(-90)" x="0" y="0" font-size="62" textLength="152" lengthAdjust="spacingAndGlyphs">DANA</text>
    <text class="surname" x="164" y="616" font-size="206" textLength="960" lengthAdjust="spacingAndGlyphs">WHITLOCK</text>
  </svg>

  <footer class="disclaimer-band">
    <p>Paid for by the Committee to Elect Dana Whitlock</p>
  </footer>
</main>
</body>
</html>
```